Kestrel Plumbing business card full re design & logo design

Kestrel Plumbing is a Sydney based mechanical plumbing contractor company.
We would like a full redesign with new logo etc which we can take to a future website, uniforms, vehicle sign writing etc.
Blue is my preferred choice of colour but i would be open to see a couple of alternatives thrown in the mix to see how they compare. I am open to see on white cards, black cards etc. Open to many new ideas.
Please see attached original business cards which have been used for the last 5 years.

Target Market(s)

Mechanical services industry.

Industry/Entity Type

Plumbing

Contact Information for Business Card

Dale Fenmore
Director

Mob: 0427 596 418
Email: dale@kestrelplumbing-demo.net.au
PO BOX 782
Ashdene NSW 2164
Lic: 518604k

Logo Text

Kestrel Plumbing

Font styles to use
Sans Serif

Colors
0655a3
3276b5
0792cd
33a6d7
85cae6
000000
333333
474747

Requirements
Must have
• Things that make it very professional and very well presented.
Nice to have
• Same description or very similar to attached uploaded file
Should not have
• Anything that makes it look unprofessional or cartoony.

```html
<!DOCTYPE html>
<html lang="en">
<head>
<meta charset="utf-8">
<title>Kestrel Plumbing – Business Card</title>
<link rel="stylesheet" href="https://fonts.googleapis.com/css2?family=Open+Sans:ital,wght@0,400;0,700;1,700&display=swap">
<style>
  :root {
    --canvas: #e6e6e6;
    --card-white: #ffffff;
    --brand-blue: #3276b5;
    --brand-deep: #0655a3;
    --brand-bright: #0792cd;
    --text-dark: #333333;
    --text-white: #ffffff;
  }
  * { margin: 0; padding: 0; box-sizing: border-box; }
  html, body {
    width: 1200px; height: 1000px; overflow: hidden;
    background: var(--canvas);
    font-family: "Open Sans", Arial, sans-serif;
  }
  .stage { position: relative; width: 1200px; height: 1000px; }

  /* Front of card */
  .card-front {
    position: absolute; left: 199px; top: 38px;
    width: 802px; height: 458px;
    background: var(--card-white);
  }
  .brand-name {
    position: absolute; left: 19px; top: 18px;
    display: flex; align-items: center; gap: 10px;
    color: var(--brand-bright);
    font-weight: 700; font-size: 36px; line-height: 1.05;
    letter-spacing: 0.5px;
  }
  .brand-dot {
    width: 14px; height: 14px; border-radius: 50%;
    background: var(--brand-bright);
  }
  .person-name {
    position: absolute; left: 19px; top: 129px;
    color: var(--brand-blue); font-weight: 700; font-size: 24px;
  }
  .person-role {
    position: absolute; left: 19px; top: 161px;
    color: var(--text-dark); font-size: 22px;
  }
  .contact-list {
    position: absolute; left: 19px; top: 213px;
    list-style: none; font-size: 22.5px; line-height: 31px;
    color: var(--text-dark);
  }
  .contact-list .label { color: var(--brand-blue); font-weight: 700; }
  .service-band {
    position: absolute; left: 0; top: 382px;
    width: 802px; height: 65px;
    background: var(--brand-blue);
    color: var(--text-white);
    display: flex; align-items: center; justify-content: center;
    font-size: 28px; letter-spacing: -0.5px;
  }
  .service-band .divider { margin: 0 9px; }

  /* Back of card */
  .card-back {
    position: absolute; left: 199px; top: 505px;
    width: 802px; height: 458px;
    background: var(--brand-blue);
    color: var(--text-white);
  }
  .back-heading {
    position: absolute; left: 0; top: 22px; width: 822px;
    text-align: center; font-weight: 700; font-size: 35.5px;
  }
  .specialties {
    position: absolute; left: 469px; top: 86px;
  }
  .specialties-title { font-weight: 700; font-size: 36px; line-height: 46px; }
  .specialties-list { list-style: none; margin-top: 2px; }
  .specialties-list li {
    position: relative; padding-left: 36px;
    font-weight: 700; font-size: 29px; line-height: 41.6px;
  }
  .specialties-list li::before {
    content: ""; position: absolute; left: 2px; top: 17px;
    width: 9px; height: 9px; background: var(--text-white);
  }
  .tagline {
    position: absolute; left: 108px; top: 396px;
    font-style: italic; font-weight: 700; font-size: 24px;
    letter-spacing: 0.6px;
  }
</style>
</head>
<body>
<main class="stage">
  <section class="card-front">
    <div class="brand-name"><span class="brand-dot"></span><span>Kestrel<br>Plumbing</span></div>
    <p class="person-name">Dale Fenmore</p>
    <p class="person-role">Director</p>
    <ul class="contact-list">
      <li><span class="label">Mob:</span> 0427 596 418</li>
      <li><span class="label">Email:</span> dale@kestrelplumbing-demo.net.au</li>
      <li><span class="label">Web:</span>www.kestrelplumbing-demo.net.au</li>
      <li><span class="label">Add:</span> PO BOX 782 Ashdene NSW 2164</li>
      <li><span class="label">Lic:</span> 518604kbing</li>
    </ul>
    <div class="service-band">
      MECHANICAL PIPING<span class="divider">|</span>CHW<span class="divider">|</span>HW<span class="divider">|</span>CW<span class="divider">|</span>REFRIG
    </div>
  </section>

  <section class="card-back">
    <h2 class="back-heading">MECHANICAL PLUMBING SERVICES</h2>
    <div class="specialties">
      <p class="specialties-title">Specialising in:</p>
      <ul class="specialties-list">
        <li>Make Good</li>
        <li>Refurbishment</li>
        <li>Tenancy Fit Out</li>
        <li>Plant Room Works</li>
        <li>Shut Downs</li>
        <li>Change Overs</li>
      </ul>
    </div>
    <p class="tagline">KESTREL have the SOLUTION</p>
  </section>
</main>
</body>
</html>
```